banner for website

I need a new banner for my website. My website now is. www.brightmeadowkitchen.net, but I'm changing it to Fresh Rooted Days and I need a new banner. I want me to be who it's about. I am my brand. I'm Marla Prewitt. So, my name needs to be prominent in the banner along with my photo, which I'm attaching. I want my photo very prominent in the banner and very large. I am attaching my two favorites.
I need the banner plain ( with out the newsletter sign up optin part), so I can use it on my newsletters, emails and letter head, as well. I would like it to be inviting. I I have a certain color scheme I use. Deep dark brown letters with blues and greens. Very earthy and psychologically grounded. I would like to keep that color scheme. In my website banner, I need a opt in to sign up for my free monthly newsletter and receive my Free Pantry Starter Booklet.

I want the shopping guide to be small and pleasant looking and to say: "Sign up to receive your Free Pantry Starter Booklet and monthly newsletter."

I only want my banner to say: "Fresh Rooted Days" "Marla Prewitt"

I would also like to have part of the banner without the sign in for the newsletter part off of it. And also one with only the "Fresh Rooted Days" and one with "Fresh Rooted Days" and "Marla Prewitt" without the newsletter sign up part on it either.

I hope you can do this for me. I look forward to seeing your design! Sincerely, Marla
Updates

Project Deadline Extended Reason: I couldn't view the designs so I couldn't look at the ones submitted. I just now got into the website with your company's help. I don't want to be penalized because of a problem with the log in at your site. That was not my fault. Please let me know your thoughts. Added Monday, May 9, 2016

Target Market(s)

people over 40 who have bad health or who want to learn how to be a vegetarian for better health.

Number of Pages Required

1 page

Requirements
Must have
• I want the shopping guide to be small and pleasant looking and to say: "Sign up to receive your Free Pantry Starter Booklet and monthly newsletter." I would like it to blend and be elegant and not in the middle of the banner or across my face.
• I only want my banner to say: "Fresh Rooted Days" "Marla Prewitt"
• I would also like to have part of the banner without the sign in for the newsletter part off of it. And also one with only the "Fresh Rooted Days" and one with "Fresh Rooted Days" and "Marla Prewitt" without the newsletter sign up part on it either.
Nice to have
• Nice font and colors. I want the background to be plants and earthy and inviting.
Should not have
• I updated and added two new photos. I think the one you were using with me in the red top looked funny under my eyes. it was too pink or something. I uploaded a better version of that photo. in hopes that it looks better. Please switch those out if you are using the one with me in the red top.

```html
<!DOCTYPE html>
<html lang="en">
<head>
<meta charset="utf-8">
<title>Fresh Rooted Days – Marla Prewitt</title>
<link rel="stylesheet" href="https://fonts.googleapis.com/css2?family=Cinzel:wght@700&family=Allura&family=Cabin+Condensed:wght@600&display=swap">
<style>
  :root {
    --brown-deep: #553629;
    --brown-mid: #7b5a4d;
    --taupe: #a89188;
    --mist: #d6ccc7;
    --white: #ffffff;
    --photo-warm: #b07a5c;
    --photo-red: #8e2f26;
    --photo-green: #5f7a3a;
  }
  html, body {
    margin: 0;
    padding: 0;
    overflow: hidden;
    background: var(--white);
  }
  .banner {
    position: relative;
    width: 1200px;
    height: 308px;
    overflow: hidden;
    background: linear-gradient(90deg, var(--brown-deep) 0%, var(--brown-mid) 38%, var(--taupe) 62%, var(--mist) 100%);
    color: var(--white);
  }
  .portrait {
    position: absolute;
    left: 0;
    top: 0;
    width: 250px;
    height: 308px;
    background:
      radial-gradient(ellipse at 45% 30%, #d9b38f 0%, var(--photo-warm) 35%, transparent 70%),
      linear-gradient(180deg, #6e4a3a 0%, var(--photo-red) 62%, var(--photo-green) 100%);
  }
  .brand {
    position: absolute;
    left: 262px;
    top: 36px;
    width: 320px;
  }
  .brand-dot {
    position: absolute;
    left: 0;
    top: 12px;
    width: 46px;
    height: 46px;
    border-radius: 50%;
    background: rgba(255, 255, 255, 0.85);
  }
  .brand-name {
    position: absolute;
    left: 58px;
    top: 14px;
    margin: 0;
    font-family: "Cinzel", serif;
    font-weight: 700;
    font-size: 34px;
    line-height: 1;
    white-space: nowrap;
    letter-spacing: 0.5px;
  }
  .owner-name {
    position: absolute;
    left: 168px;
    top: 64px;
    margin: 0;
    font-family: "Allura", cursive;
    font-size: 48px;
    line-height: 1;
    white-space: nowrap;
  }
  .optin {
    position: absolute;
    left: 770px;
    top: 18px;
    width: 410px;
    margin: 0;
    text-align: center;
    font-family: "Cabin Condensed", sans-serif;
    font-weight: 600;
    font-size: 33px;
    line-height: 39px;
  }
  .optin .script {
    font-family: "Allura", cursive;
    font-weight: 400;
    font-size: 40px;
  }
</style>
</head>
<body>
  <div class="banner">
    <div class="portrait" role="img" aria-label="Photo of Marla Prewitt holding a basket of fresh garden vegetables"></div>

    <div class="brand">
      <span class="brand-dot"></span>
      <h1 class="brand-name">Fresh Rooted Days</h1>
      <p class="owner-name">Marla Prewitt</p>
    </div>

    <p class="optin">
      Sign up to recieve <span class="script">Marla's</span><br>
      monthly newsletter<br>
      + a <span class="script">free</span> pantry starter booklet!
    </p>
  </div>
</body>
</html>
```